SLA & Internet Advert

Advertise some of our key SLA services & Internet Connectivity services.
Service Level Agreement:
Unlimited Remote, Email, Helpdesk & Telephone Support.
Unlimited Service Calls
Support Hours Monday - Saturday 7am-10pm Sunday till 5pm
Free additional visits during ofsted periods
Free remote access to school server for staff members
Free mobile device management for tablet devices
Free Email&Webhosting Service
Remote support on every device in school allowing us to close 90% of tickets within 30 mins.
Service Level Agreement Package 1 - Includes all the above + 1 Site visit every 2 weeks £2,500 per annum
Service Level Agreement Package 2 - Includes all the above + 1 Site Visit every week £4,500 per annum
Service Level Agreement Package 3 - Includes all the above + 2 Site visits every week - £7,540 per annum
Internet Connectivity (medium/large Primary)
Managed Firewall
Managed Web filter & Safeguarding
User reporting portal/email reporting.
Main Internet Line 1000 mb/s download 100mb/s upload
Back up Internet Line 80mb/s download 20mb/s upload
100% uptime guaranteed.
£3000 per annum
Internet Connectivity (Small Primary School)
Managed Firewall
£2100 per annum
My website is https://www.lumora-net.co.uk if you need any further information like phone numbers / email address etc
Target Market(s)
Education
Look and feel
Each slider illustrates characteristics of the customer's brand and the style your logo design should communicate.

```html
<!DOCTYPE html>
<html lang="en">
<head>
<meta charset="utf-8">
<title>SLA &amp; Internet Connectivity Services – Lumora Net</title>
<link href="https://fonts.googleapis.com/css2?family=PT+Sans:wght@400;700&family=Source+Sans+3:wght@300;400;600;700&display=swap" rel="stylesheet">
<style>
  :root{
    --blue:#1d5fae;
    --blue-dark:#0f4896;
    --blue-deep:#0b3a7d;
    --orange:#f07e40;
    --orange-text:#ef7a36;
    --sky:#d6ebf9;
    --sky-light:#eef7fd;
    --ink:#2f3440;
    --page:#e6e7e9;
    --white:#ffffff;
  }
  *{box-sizing:border-box;margin:0;padding:0}
  html,body{width:1200px;height:1085px;overflow:hidden;background:var(--page)}
  body{font-family:"Source Sans 3",sans-serif;color:var(--ink)}
  .flyer{position:absolute;left:232px;top:20px;width:735px;height:1046px;overflow:hidden;
    background:linear-gradient(180deg,var(--sky) 0%,var(--sky-light) 60%,var(--white) 100%);
    box-shadow:0 4px 18px rgba(0,0,0,.18)}
  .top-band{position:absolute;left:0;top:0;width:100%;height:345px;
    background:linear-gradient(180deg,#2a63b4 0%,var(--blue) 100%)}
  .hero{position:absolute;left:28px;top:48px;width:670px;height:447px;border:4px solid var(--orange);
    border-radius:46px;overflow:hidden;background:var(--white);padding:4px}
  .hero-photo{width:100%;height:100%;border-radius:40px;
    background:linear-gradient(135deg,#e7eef3 0%,#c7dcea 35%,#f1c9a8 60%,#3fa3c8 85%,#e6f1f6 100%)}
  .side-panel{position:absolute;left:418px;top:421px;right:0;bottom:0;background:var(--orange);
    border-top-left-radius:52px}
  .badge{position:absolute;left:570px;top:331px;width:146px;height:146px;border-radius:50%;
    background:radial-gradient(circle at 40% 35%,#2a6cc0 0%,var(--blue-deep) 75%);
    border:2px dashed #8fb5e3;outline:3px solid var(--blue-deep);
    display:flex;align-items:center;justify-content:center;text-align:center;
    font-family:"PT Sans",sans-serif;font-weight:700;font-size:15.5px;line-height:19px;color:var(--white)}
  .headline{position:absolute;left:32px;top:500px;font-family:"PT Sans",sans-serif;font-weight:700;
    font-size:20px;line-height:19px;color:var(--orange-text)}
  .pill{position:absolute;background:var(--blue);color:var(--white);border-radius:0 22px 22px 22px;
    font-family:"PT Sans",sans-serif;font-weight:700}
  .sla-pill{left:18px;top:552px;width:259px;height:33px;border-radius:20px 20px 20px 4px;
    font-size:16px;line-height:33px;padding-left:11px}
  .bullets{position:absolute;list-style:none;font-weight:300;font-size:13px;line-height:18px}
  .bullets li{position:relative;padding-left:18px}
  .bullets li::before{content:"";position:absolute;left:0;top:4px;width:9px;height:9px;border-radius:50%;background:var(--blue)}
  .bullets li::after{content:"";position:absolute;left:2px;top:6.5px;width:3px;height:3px;
    border-top:1.2px solid var(--white);border-right:1.2px solid var(--white);transform:rotate(45deg)}
  .sla-list{left:32px;top:596px;width:360px}
  .remote-note{position:absolute;left:32px;top:752px;font-weight:600;font-size:14px;line-height:18px;color:var(--blue)}
  .packages{position:absolute;left:28px;top:808px;display:flex;gap:11px}
  .package{width:113px;height:96px;border:1px dashed var(--blue);border-radius:6px;background:var(--white);
    text-align:center;overflow:hidden}
  .package-head{background:var(--blue);color:var(--white);font-family:"PT Sans",sans-serif;font-weight:700;
    font-size:10.5px;line-height:12px;padding:4px 0 3px}
  .package-head small{display:block;font-size:6px;line-height:8px}
  .package-body{font-size:7.5px;line-height:12px;margin-top:7px;color:var(--ink)}
  .package-price{display:inline-block;margin-top:8px;background:var(--blue);color:var(--white);
    border-radius:0 8px 0 8px;font-weight:700;font-size:10px;line-height:18px;padding:0 7px}
  .package-price small,.price small{font-size:.6em;text-transform:uppercase}
  .brand{position:absolute;left:24px;top:955px}
  .brand-name{display:flex;align-items:center;gap:8px;font-family:"PT Sans",sans-serif;font-weight:700;
    font-size:38px;line-height:40px;color:var(--orange-text);letter-spacing:1px}
  .brand-mark{width:30px;height:30px;background:var(--orange-text)}
  .brand-tag{font-size:12.5px;letter-spacing:1.6px;color:var(--blue);margin-top:6px;font-weight:400}
  .net-pill{left:401px;width:259px;height:39px;border-radius:22px;display:flex;align-items:center;gap:7px;padding-left:9px}
  .net-pill svg{flex:none}
  .net-pill h3{font-size:16px;line-height:16px}
  .net-pill span{display:block;font-weight:400;font-size:13px;line-height:14px;font-family:"Source Sans 3",sans-serif}
  .net-list{color:var(--white);font-size:13px;line-height:18.4px;width:290px;left:439px}
  .net-list li::before{background:var(--blue)}
  .price{position:absolute;left:437px;width:121px;height:27px;background:var(--blue);color:var(--white);
    border-radius:0 12px 0 12px;font-weight:700;font-size:15px;line-height:27px;padding-left:7px}
  .contact-bar{position:absolute;left:299px;top:966px;right:0;height:51px;background:var(--blue);
    border-radius:26px 0 0 26px;display:flex;align-items:center;gap:15px;padding-left:22px;
    color:var(--white);font-size:12.5px;font-weight:600}
  .contact-bar span{display:flex;align-items:center;gap:5px}
</style>
</head>
<body>
<main class="flyer">
  <div class="top-band"></div>
  <div class="hero"><div class="hero-photo" role="img" aria-label="Photo of four school children gathered around a laptop in a classroom"></div></div>
  <div class="side-panel"></div>
  <div class="badge">WE OFFER<br>FAST, FLEXIBLE,<br>RELIABLE<br>ICT SUPPORT</div>

  <h1 class="headline">SLA SERVICES &amp;<br>INTERNET CONNECTIVITY SERVICES</h1>
  <h2 class="pill sla-pill">SERVICE LEVEL AGREEMENT:</h2>
  <ul class="bullets sla-list">
    <li>Unlimited Remote, Email, Helpdesk &amp; Telephone Support</li>
    <li>Unlimited Service Calls</li>
    <li>Support Hours Monday - Saturday 7am-10pm<br>Sunday till 5pm</li>
    <li>Free additional visits during ofsted periods</li>
    <li>Free remote access to school server for staff members</li>
    <li>Free mobile device management for tablet devices</li>
    <li>Free Email &amp; Webhosting Service</li>
  </ul>
  <p class="remote-note">Remote support on every device in school<br>allowing us to close 90% of tickets within 30 mins.</p>

  <section class="packages">
    <div class="package"><div class="package-head">PACKAGE 1<small>SERVICE LEVEL AGREEMENT</small></div>
      <p class="package-body">Includes all the above<br>+ 1 Site visit every 2 weeks</p>
      <span class="package-price">£2,500 <small>per annum</small></span></div>
    <div class="package"><div class="package-head">PACKAGE 2<small>SERVICE LEVEL AGREEMENT</small></div>
      <p class="package-body">Includes all the above<br>+ 1 Site Visit every week</p>
      <span class="package-price">£4,500 <small>per annum</small></span></div>
    <div class="package"><div class="package-head">PACKAGE 3<small>SERVICE LEVEL AGREEMENT</small></div>
      <p class="package-body">Includes all the above<br>+ 2 Site visits every week</p>
      <span class="package-price">£7,540 <small>per annum</small></span></div>
  </section>

  <div class="pill net-pill" style="top:503px">
    <svg width="28" height="28" viewBox="0 0 28 28" fill="none" stroke="#fff" stroke-width="1.6"><circle cx="14" cy="14" r="12"/><ellipse cx="14" cy="14" rx="5" ry="12"/><path d="M2 14h24M4 8h20M4 20h20"/></svg>
    <h3>INTERNET CONNECTIVITY<span>(Medium/Large Primary)</span></h3>
  </div>
  <ul class="bullets net-list" style="top:560px">
    <li>Managed Firewall</li>
    <li>Managed Web filter &amp; Safeguarding</li>
    <li>User reporting portal/email reporting.</li>
    <li>Main Internet Line 1000 mb/s download<br>100mb/s upload</li>
    <li>Back up Internet Line 80mb/s download<br>20mb/s upload</li>
    <li>100% uptime guaranteed</li>
  </ul>
  <div class="price" style="top:709px">£3000 <small>per annum</small></div>

  <div class="pill net-pill" style="top:767px">
    <svg width="28" height="28" viewBox="0 0 28 28" fill="none" stroke="#fff" stroke-width="1.6"><circle cx="14" cy="14" r="12"/><ellipse cx="14" cy="14" rx="5" ry="12"/><path d="M2 14h24M4 8h20M4 20h20"/></svg>
    <h3>INTERNET CONNECTIVITY<span>(Small Primary School)</span></h3>
  </div>
  <ul class="bullets net-list" style="top:824px">
    <li>Managed Firewall</li>
    <li>Managed Web filter &amp; Safeguarding</li>
    <li>User reporting portal/email reporting.</li>
    <li>Main Internet Line 1000 mb/s download<br>100mb/s upload</li>
  </ul>
  <div class="price" style="top:922px">£2100 <small>per annum</small></div>

  <div class="brand">
    <div class="brand-name"><span class="brand-mark"></span>LUMORA NET</div>
    <div class="brand-tag">EDUCATION SUPPORT &amp; INSTALLATION</div>
  </div>

  <footer class="contact-bar">
    <span><svg width="14" height="14" viewBox="0 0 14 14"><circle cx="7" cy="7" r="7" fill="#f07e40"/><path d="M4.5 3.5l1.5 0 .6 1.8-.9.7a5 5 0 0 0 2.3 2.3l.7-.9 1.8.6v1.5c-3.5.3-6.3-2.5-6-6z" fill="#fff"/></svg>0161 555 0142</span>
    <span><svg width="14" height="14" viewBox="0 0 14 14"><circle cx="7" cy="7" r="7" fill="#f07e40"/><rect x="3.5" y="4.5" width="7" height="5" fill="none" stroke="#fff" stroke-width="1"/><path d="M3.5 4.5l3.5 3 3.5-3" fill="none" stroke="#fff" stroke-width="1"/></svg>info@lumora-net.co.uk</span>
    <span><svg width="14" height="14" viewBox="0 0 14 14" fill="none"><circle cx="7" cy="7" r="7" fill="#f07e40"/><circle cx="7" cy="7" r="4" stroke="#fff"/><path d="M3 7h8M7 3v8" stroke="#fff" stroke-width=".8"/></svg>www.lumora-net.co.uk</span>
  </footer>
</main>
</body>
</html>
```